Bright Towns Alliance PowerPoint Design Template and Sample Deck

The Bright Towns Alliance is an international organization that seeks to improve the livability, workability and sustainability of the world’s cities.
We seek a versatile PowerPoint design template with 10 slide types plus a “self-documenting” sample deck. Your design will be used in keynote speeches and workshops around the world.
After the contest is completed, we will ask the winning designer to add 10-20 additional slide types for $75 per slide. We also seek a long-term relationship whereby we can request “custom” slides and/or ask the designer to touch up the slides we build to make them better.
FILES. We have uploaded several files:
1. BRIGHT TOWNS ALLIANCE DESIGN CONTEST NOTES.docx with full instructions.
2. PALETTE. Shows our official colors.
3 LOGOS. Several individual files with different variations of our logo. Some with our motto, some without.
2. SAMPLE SLIDES. Because we were unable to successfully upload our sample deck, we are making it available via this FileCrate link:
https://www.filecrate-example.net/s/k7qvmr2tn8wzd4h/The%20Bright%20Towns%20Alliance%20Design%20Contest%20Notes.docx?dl=0
Target Market(s)
Mayors, department heads, CIOs, senior executives from technology companies
Industry/Entity Type
Information Technology
Colors
Designer to choose colors to be used in the design.
Requirements
Must have
- Please see uploaded Word document for requirements, nice to haves and should not haves and uploaded palette for color preferences.
Nice to have
- see above
Should not have
- see above

```html
<!DOCTYPE html>
<html lang="en">
<head>
<meta charset="utf-8">
<title>Bright Towns Alliance – Slide 3</title>
<link rel="stylesheet" href="https://fonts.googleapis.com/css2?family=Carlito:wght@400;700&display=swap">
<style>
  :root {
    --brand-blue: #00468b;
    --navy: #0b3361;
    --accent-orange: #f7941d;
    --ring-grey: #8a8a8a;
    --text-dark: #1a1a1a;
    --white: #ffffff;
    --photo-dark: #2b2d31;
    --photo-mid: #4a4c50;
  }
  * { box-sizing: border-box; margin: 0; padding: 0; }
  html, body { width: 1200px; height: 675px; overflow: hidden; background: var(--white); }
  body { font-family: "Carlito", "Calibri", sans-serif; }

  .slide { position: relative; width: 1200px; height: 675px; background: var(--white); overflow: hidden; }

  .hero-photo {
    position: absolute; left: 0; top: 0; width: 553px; height: 675px;
    background: linear-gradient(160deg, var(--photo-mid) 0%, var(--photo-dark) 55%, #3b3d40 100%);
  }
  .hero-title {
    position: absolute; left: 61px; top: 312px;
    color: var(--white); font-weight: 700; font-size: 50px; letter-spacing: 0.5px;
  }

  .feature-icon { position: absolute; left: 492px; width: 160px; height: 160px; }
  .feature-icon.first  { top: 79px; }
  .feature-icon.second { top: 256px; }
  .feature-icon.third  { top: 434px; }

  .feature-text {
    position: absolute; left: 674px; width: 480px;
    font-size: 19.5px; line-height: 25px; color: var(--text-dark);
  }
  .feature-text strong { color: var(--navy); font-weight: 700; }
  .feature-text.first  { top: 129px; }
  .feature-text.second { top: 305px; }
  .feature-text.third  { top: 491px; }

  .page-number {
    position: absolute; left: 1090px; top: 623px; width: 50px; height: 50px;
    border-radius: 50%; background: var(--navy); color: var(--white);
    font-size: 15px; display: flex; align-items: center; justify-content: center;
  }
</style>
</head>
<body>
<main class="slide">
  <div class="hero-photo" role="img" aria-label="Dark-toned photo of hands typing on a laptop keyboard"></div>
  <h1 class="hero-title">LOREM IPSUM</h1>

  <svg class="feature-icon first" viewBox="0 0 160 160" aria-hidden="true">
    <path d="M80 5 A75 75 0 0 1 80 155" fill="none" stroke="var(--ring-grey)" stroke-width="4"/>
    <circle cx="75" cy="80" r="75" fill="var(--white)"/>
    <circle cx="75" cy="80" r="67" fill="var(--brand-blue)"/>
    <rect x="38" y="60" width="74" height="38" rx="16" fill="var(--accent-orange)" role="img" aria-label="Handshake icon"/>
  </svg>

  <svg class="feature-icon second" viewBox="0 0 160 160" aria-hidden="true">
    <path d="M80 5 A75 75 0 0 1 80 155" fill="none" stroke="var(--ring-grey)" stroke-width="4"/>
    <circle cx="75" cy="80" r="75" fill="var(--white)"/>
    <circle cx="75" cy="80" r="67" fill="var(--brand-blue)"/>
    <rect x="48" y="24" width="56" height="112" rx="14" fill="var(--accent-orange)" role="img" aria-label="Two business people standing together"/>
  </svg>

  <svg class="feature-icon third" viewBox="0 0 160 160" aria-hidden="true">
    <path d="M80 5 A75 75 0 0 1 80 155" fill="none" stroke="var(--ring-grey)" stroke-width="4"/>
    <circle cx="75" cy="80" r="75" fill="var(--white)"/>
    <circle cx="75" cy="80" r="67" fill="var(--brand-blue)"/>
    <g fill="none" stroke="var(--accent-orange)" stroke-width="3" stroke-linejoin="round" stroke-linecap="round">
      <path d="M45 40 H83 L99 56 V112 H45 Z"/>
      <path d="M83 40 V56 H99"/>
      <circle cx="76" cy="90" r="11" stroke-width="4"/>
      <path d="M84 98 L98 112" stroke-width="6"/>
    </g>
  </svg>

  <p class="feature-text first"><strong>Lorem Ipsum</strong> is simply dummy text of the printing and typesetting industry.</p>
  <p class="feature-text second"><strong>Lorem Ipsum</strong> is simply dummy text of the printing and typesetting industry.</p>
  <p class="feature-text third"><strong>Lorem Ipsum</strong> is simply dummy text of the printing and typesetting industry.</p>

  <div class="page-number">3</div>
</main>
</body>
</html>
```